Brightwell Homes Guide Business card

I have had at the logo designed here and attached. The business compares off the plan apartments in Sydney and provides quick comparison for new home buyers e.g price, floor plans and location. I would like the complimentary colours used on the business card. I would like it be unique but also look professional. I also have a website to gain inspiration from www.brightwellhomesguide.com.au
Updates
Industry/Entity Type
Business
Contact Information for Business Card
Helen Vostrakis
Director of Business Development
e: helen.vostrakis@brightwellhomesguide.com.au
p: (02) 8143 7692
m: 0431 572 908
w: www.brightwellhomesguide.com.au
Look and feel
Each slider illustrates characteristics of the customer's brand and the style your logo design should communicate.

```html
<!DOCTYPE html>
<html lang="en">
<head>
<meta charset="utf-8">
<title>Brightwell Homes Guide – Business Card</title>
<link rel="stylesheet" href="https://fonts.googleapis.com/css2?family=Open+Sans:wght@400;700&display=swap">
<style>
  :root {
    --backdrop: #2b2b2d;
    --card-black: #0d0d0e;
    --card-back: #151516;
    --brand-green: #7ed03a;
    --text-light: #d9d9d9;
    --text-muted: #9a9a9a;
  }
  * { box-sizing: border-box; margin: 0; padding: 0; }
  html, body {
    width: 1200px; height: 716px; overflow: hidden;
    background: var(--backdrop);
    font-family: "Open Sans", Arial, sans-serif;
  }
  .stage {
    width: 1200px; height: 716px;
    display: flex; align-items: center; justify-content: center; gap: 60px;
  }
  .card {
    position: relative;
    width: 510px; height: 312px;
    overflow: hidden;
    box-shadow: 0 14px 40px rgba(0,0,0,.45);
  }
  /* Back face */
  .card-back { background: var(--card-back); }
  .back-pattern {
    position: absolute; inset: 0;
    background: linear-gradient(135deg, #191919 0%, #121212 100%);
  }
  .back-brand {
    position: absolute; left: 50%; top: 50%;
    transform: translate(-50%, -50%);
    display: flex; align-items: center; gap: 10px;
    font-size: 20px; font-weight: 400; color: #bfbfbf;
    white-space: nowrap;
  }
  .brand-square { width: 14px; height: 14px; background: currentColor; flex: none; }

  /* Front face */
  .card-front { background: var(--card-black); }
  .brand-name {
    position: absolute; left: 122px; top: 42px;
    display: flex; align-items: center; gap: 10px;
    font-size: 24px; font-weight: 400; color: var(--brand-green);
    white-space: nowrap;
  }
  .brand-name .brand-square { width: 20px; height: 20px; }
  .person { position: absolute; left: 42px; top: 104px; }
  .person-name {
    font-size: 21px; font-weight: 700; color: var(--brand-green);
    text-transform: uppercase; letter-spacing: .3px; line-height: 1.2;
  }
  .person-role { font-size: 11px; color: var(--text-muted); margin-top: 1px; }
  .contacts {
    position: absolute; left: 42px; top: 160px;
    list-style: none;
  }
  .contacts li {
    display: flex; align-items: center; gap: 8px;
    font-size: 13px; color: var(--text-light); line-height: 21px;
    white-space: nowrap;
  }
  .contacts .sep { color: var(--brand-green); margin: 0 4px; }
  .icon { width: 13px; height: 13px; flex: none; }
  .accent-band { position: absolute; left: 0; top: 232px; width: 510px; height: 40px; }
</style>
</head>
<body>
<main class="stage">
  <section class="card card-back" aria-label="Business card, back">
    <div class="back-pattern" role="img" aria-label="Subtle tonal repeating brand pattern on black"></div>
    <div class="back-brand"><span class="brand-square"></span>Brightwell Homes Guide</div>
  </section>

  <section class="card card-front" aria-label="Business card, front">
    <div class="brand-name"><span class="brand-square"></span>Brightwell Homes Guide</div>

    <div class="person">
      <p class="person-name">Helen Vostrakis</p>
      <p class="person-role">Director of Business Development</p>
    </div>

    <ul class="contacts">
      <li>
        <svg class="icon" viewBox="0 0 14 14"><rect width="14" height="14" rx="2" fill="#7ed03a"/><path d="M4 3.5l1.6-.3.9 2-1 .8a6 6 0 0 0 2.6 2.6l.8-1 2 .9-.3 1.6C7.5 10.4 3.6 6.5 4 3.5z" fill="#0d0d0e"/></svg>
        <span>(02) 8143 7692<span class="sep">|</span>0431 572 908</span>
      </li>
      <li>
        <svg class="icon" viewBox="0 0 14 14"><rect width="14" height="14" rx="2" fill="#7ed03a"/><rect x="3" y="4.5" width="8" height="5.5" fill="#0d0d0e"/><path d="M3 4.5l4 3 4-3" stroke="#7ed03a" stroke-width="1" fill="none"/></svg>
        helen.vostrakis@brightwellhomesguide.com.au
      </li>
      <li>
        <svg class="icon" viewBox="0 0 14 14"><rect width="14" height="14" rx="2" fill="#7ed03a"/><circle cx="7" cy="7" r="3.6" stroke="#0d0d0e" stroke-width="1.2" fill="none"/><path d="M3.4 7h7.2M7 3.4v7.2" stroke="#0d0d0e" stroke-width="1"/></svg>
        www.brightwellhomesguide.com.au
      </li>
    </ul>

    <svg class="accent-band" viewBox="0 0 510 40" preserveAspectRatio="none" aria-hidden="true">
      <polygon points="0,4 330,4 300,24 0,24" fill="#7ed03a"/>
    </svg>
  </section>
</main>
</body>
</html>
```